GIlbeto Shop Business Card Design

My auto shop is targeted to the European and Asian luxury automotive market. We do mechanics collision and parts.
Some of the makes are KRT, DZ, Vale Strider, Quendel,Morva, solvana, telira, RP, etc. But in the end we get all makes.
I don't want to have the makes logos on the business card.
The Name of the business is after my first Name Gilberto but without the s Gilbeto Shop if there is any other ideas about the name iam open to suggestions. And i don't have a LOGO. Need logo!

Reason: I increased my budget and invited more designers. And committed payment so giving you guys more time.

Target Market(s)

target is the luxury auto market

Industry/Entity Type

Automotive

Contact Information for Business Card

European Automotive Repair Shop, Collision Mechanics Parts
Gilberto Montaño Owner, Pinoverde #9 Loma Seca 2

Requirements
Nice to have
• One design i can of liked was the use of the dash error logos like check engine light airbag light. Nordel press has this but dose not include the air bag light. For the collision part of the business. But am open to any design.
Should not have
• exact logo makes on front of card.

```html
<!DOCTYPE html>
<html lang="en">
<head>
<meta charset="utf-8">
<title>Gilbeto Shop Business Card</title>
<link rel="stylesheet" href="https://fonts.googleapis.com/css2?family=Open+Sans:ital,wght@0,400;0,600;0,700;0,800;1,700&display=swap">
<style>
  :root {
    --backdrop: #8e8e8e;
    --paper: #ffffff;
    --charcoal: #3a3a3a;
    --ink: #2b2b2b;
    --amber: #f2b84b;
    --icon-tone: rgba(255, 255, 255, 0.14);
  }
  * { margin: 0; padding: 0; box-sizing: border-box; }
  html, body {
    width: 1184px;
    height: 1200px;
    overflow: hidden;
    background: var(--backdrop);
    font-family: "Open Sans", Arial, sans-serif;
  }
  .canvas { position: relative; width: 1184px; height: 1200px; }

  .card {
    position: absolute;
    left: 168px;
    width: 835px;
    height: 509px;
    background: var(--paper);
    box-shadow: 14px 14px 18px rgba(0, 0, 0, 0.35);
    overflow: hidden;
  }
  .card--front { top: 72px; }
  .card--back { top: 649px; height: 508px; }

  .wordmark {
    position: absolute;
    left: 0;
    width: 100%;
    display: flex;
    align-items: center;
    justify-content: center;
    gap: 22px;
    color: var(--ink);
    font-weight: 800;
    letter-spacing: 2px;
    text-transform: uppercase;
    white-space: nowrap;
  }
  .wordmark__square { background: var(--ink); flex: none; }
  .card--front .wordmark { top: 180px; font-size: 88px; line-height: 1; }
  .card--front .wordmark__square { width: 62px; height: 62px; }
  .card--back .wordmark { top: 52px; font-size: 70px; line-height: 1; }
  .card--back .wordmark__square { width: 50px; height: 50px; }

  .tagline-band {
    position: absolute;
    left: 0; bottom: 0;
    width: 100%;
    height: 85px;
    background: var(--charcoal);
  }
  .tagline-band__text {
    position: absolute;
    left: 27px;
    top: 19px;
    color: var(--amber);
    font-size: 34px;
    font-weight: 700;
    font-style: italic;
  }

  .details {
    position: absolute;
    left: 0; top: 227px;
    width: 100%;
    height: 251px;
    background: var(--charcoal);
  }
  .services {
    position: absolute;
    left: 24px; right: 34px; top: 24px;
    display: flex;
    align-items: center;
    gap: 12px;
  }
  .services__rule { flex: 1; height: 3px; background: var(--amber); }
  .services__text {
    color: var(--amber);
    font-size: 21px;
    font-weight: 700;
    font-style: italic;
    white-space: nowrap;
  }
  .contact { position: absolute; left: 66px; top: 68px; color: var(--amber); }
  .contact__row { display: flex; align-items: center; }
  .contact__name { font-size: 30px; font-weight: 400; gap: 12px; margin-bottom: 14px; }
  .contact__line { font-size: 18px; font-weight: 400; gap: 18px; margin-bottom: 8px; margin-left: 6px; }
  .contact svg { flex: none; fill: var(--amber); }

  .warning-lights {
    position: absolute;
    left: 355px; top: 64px;
    width: 440px; height: 113px;
    background: var(--icon-tone);
  }

  .footer-strip { position: absolute; left: 0; bottom: 0; width: 835px; height: 31px; }
  .footer-strip__text {
    position: absolute;
    left: 33px; bottom: 1px;
    color: var(--ink);
    font-size: 25px;
    font-weight: 700;
    font-style: italic;
    line-height: 31px;
  }
</style>
</head>
<body>
<main class="canvas">

  <section class="card card--front">
    <div class="wordmark"><span class="wordmark__square"></span>Gilbeto Shop</div>
    <div class="tagline-band">
      <p class="tagline-band__text">European Automotive Repair Shop</p>
    </div>
  </section>

  <section class="card card--back">
    <div class="wordmark"><span class="wordmark__square"></span>Gilbeto Shop</div>

    <div class="details">
      <div class="services">
        <span class="services__rule"></span>
        <p class="services__text">Collision Mechanics Parts Gilberto Montaño Owner</p>
        <span class="services__rule"></span>
      </div>

      <div class="contact">
        <p class="contact__row contact__name">
          <svg width="28" height="36" viewBox="0 0 28 36" aria-hidden="true">
            <circle cx="14" cy="9" r="8"/>
            <path d="M0 36 V28 Q0 19 9 19 H19 Q28 19 28 28 V36 Z"/>
          </svg>
          Professor K
        </p>
        <p class="contact__row contact__line">
          <svg width="20" height="22" viewBox="0 0 20 22" aria-hidden="true">
            <path d="M4 1 L8 6 L6 9 Q8 13 12 15 L14 13 L19 17 L16 21 Q5 19 1 5 Z"/>
          </svg>
          555 014 2837
        </p>
        <p class="contact__row contact__line">
          <svg width="30" height="26" viewBox="0 0 30 26" aria-hidden="true">
            <path d="M15 1 L29 13 H25 V25 H18 V17 H12 V25 H5 V13 H1 Z"/>
          </svg>
          Pinoverde #9 Loma Seca 2
        </p>
      </div>

      <div class="warning-lights" role="img" aria-label="Row of dashboard warning light symbols such as check engine, oil, battery, hazard, brake, airbag and ABS"></div>
    </div>

    <svg class="footer-strip" viewBox="0 0 835 31" aria-hidden="true">
      <rect x="0" y="0" width="835" height="31" fill="var(--charcoal)"/>
      <polygon points="0,0 532,0 518,31 0,31" fill="var(--amber)"/>
      <polygon points="567,0 835,0 835,31 542,31" fill="var(--amber)"/>
    </svg>
    <p class="footer-strip__text">European Automotive Repair Shop</p>
  </section>

</main>
</body>
</html>
```